Guiding the Evergreen Young Competitor:
A Family Roadmap for Nurturing Bold, Steady, and Resilient Daughters on Fields and Beyond.
📘 Book Cover Design Brief – “Guiding the Evergreen Young Competitor”

Project Title:
Design a bold, inspiring book cover for a best-selling book titled:
Guiding the Evergreen Young Competitor
Subtitle: A Family Roadmap for Nurturing Bold, Steady, and Resilient Daughters on Fields and Beyond

🎯 Audience:

Parents of female athletes ages 14–20 who want their daughters to build confidence, strength, resilience, and long-term success both in sports and in life.

This book should feel encouraging, empowering, and credible — NOT cheesy, childish, or overly academic.

📕 Design Tone & Style:

Powerful and professional — should feel like a best-selling book from a leading performance or parenting expert

Emotionally compelling — conveys hope, resilience, strength, and possibility

Visually modern and clean — avoid anything overly busy, cliché, or childish

Heroic/aspirational tone — think transformation, leadership, strong positioning

💡 Visual Direction / Ideas (Use as Inspiration, Not Limitation):

Strong, confident teenage female athlete imagery — adaptable beyond one specific sport

Symbolic visuals — e.g. athlete standing strong, on a starting line, looking bold into the future, silhouette, or power stance

Bold typography that feels clean and modern (e.g., Proxima Nova, Montserrat, Gotham, Bebas Neue, etc.)

A title that stands out clearly when viewed as a thumbnail on Bookvale

Color tones: Empowering, modern, and strong: think deep blues, greens, purples, or golds — avoid playful pastels or overly girly themes

Potential imagery: textured backgrounds, motion, bravery, development, strength, growth, sport/action overlays

🔥 What the Cover MUST Communicate:

✅ This is for parents who want strong, confident female athletes
✅ It’s a guidebook for personal development AND sports performance
✅ It’s about creating “UNSHAKEABLE” confidence — physically, mentally and emotionally
✅ The message is: You can help your daughter become her strongest, most confident self

📚 Back-of-Book Summary (for context):

"Guiding the Evergreen Young Competitor" is a parent's blueprint to building girls who are strong in body, confident in mind, and ready to lead on and off the field. Through simple strategies around strength training, mindset, nutrition, and character development, this book gives parents the tools to help their daughters stay injury-resistant, break through mental barriers, and unlock their full potential — in sports and in life.

✅ Deliverables:

Full cover design (front, back, spine) for paperback
High-resolution files (print-ready)
Source files (PSD, AI, etc.)
3D mockup versions of the book (standing, flat, stack)

Target Market(s)

Industry/Entity Type

Fitness

Font styles to use
Sans Serif

Colors
FFF300
FFF600
FEFA6F
FFFEC7
FFFEE8

Requirements
Must have
• Bold Font
Should not have
• I don't want an image of a female athlete. I want this to be font based.

```html
<!DOCTYPE html>
<html lang="en">
<head>
<meta charset="utf-8">
<title>Guiding the Evergreen Young Competitor – Book Cover</title>
<link rel="stylesheet" href="https://fonts.googleapis.com/css2?family=Bebas+Neue&family=Montserrat:wght@400;700&display=swap">
<style>
  :root {
    --page: #ffffff;
    --navy-deep: #0e141d;
    --navy-mid: #13233a;
    --navy-glow: #0f2945;
    --gold-edge: #c4a042;
    --gold-light: #e6d0a0;
    --ink-light: #ffffff;
  }
  * { margin: 0; padding: 0; box-sizing: border-box; }
  html, body {
    width: 1200px; height: 1200px; overflow: hidden;
    background: var(--page);
  }
  .book-cover {
    position: absolute;
    left: 222px; top: 31px;
    width: 763px; height: 1144px;
    background:
      radial-gradient(ellipse 60% 45% at 50% 50%, var(--navy-glow) 0%, var(--navy-mid) 45%, var(--navy-deep) 100%);
    overflow: hidden;
  }
  .book-cover svg { display: block; width: 100%; height: 100%; }
  .imprint-name {
    font-family: "Montserrat", sans-serif;
    font-weight: 700;
    fill: var(--ink-light);
  }
  .title-lead {
    font-family: "Montserrat", sans-serif;
    font-weight: 400;
    font-size: 52px;
    letter-spacing: 4px;
    fill: var(--ink-light);
  }
  .title-main {
    font-family: "Bebas Neue", sans-serif;
  }
  .subtitle {
    font-family: "Montserrat", sans-serif;
    font-weight: 400;
    font-size: 20px;
    letter-spacing: 0.8px;
    fill: var(--ink-light);
  }
  .author {
    font-family: "Bebas Neue", sans-serif;
    font-size: 56px;
    fill: var(--ink-light);
  }
</style>
</head>
<body>
  <div class="book-cover">
    <svg viewBox="0 0 763 1144" xmlns="http://www.w3.org/2000/svg">
      <defs>
        <linearGradient id="goldSheen" x1="0" y1="0" x2="1" y2="0">
          <stop offset="0" stop-color="var(--gold-edge)"/>
          <stop offset="0.5" stop-color="var(--gold-light)"/>
          <stop offset="1" stop-color="var(--gold-edge)"/>
        </linearGradient>
      </defs>

      <!-- imprint -->
      <g class="imprint">
        <circle cx="613" cy="128" r="42" fill="none" stroke="var(--gold-edge)" stroke-width="3"/>
        <text class="imprint-name" x="613" y="204" text-anchor="middle" font-size="17" letter-spacing="3">EVERGREEN</text>
        <text class="imprint-name" x="613" y="225" text-anchor="middle" font-size="17" letter-spacing="3">COMPETITOR</text>
      </g>

      <!-- title -->
      <text class="title-lead" x="381.5" y="352" text-anchor="middle">GUIDING THE</text>
      <text class="title-main" x="87" y="536" font-size="200" textLength="587" lengthAdjust="spacingAndGlyphs" fill="url(#goldSheen)">EVERGREEN</text>
      <text class="title-main" x="87" y="651" font-size="112" textLength="587" lengthAdjust="spacingAndGlyphs" fill="url(#goldSheen)">YOUNG COMPETITOR</text>

      <!-- chevron -->
      <path d="M363 734 L382 716 L401 734 L395 737 L382 725 L369 737 Z" fill="var(--gold-edge)"/>

      <!-- subtitle -->
      <text class="subtitle" x="381.5" y="798" text-anchor="middle">A Family Roadmap for Nurturing Bold, Steady,</text>
      <text class="subtitle" x="381.5" y="827" text-anchor="middle">and Resilient Daughters on Fields and Beyond</text>

      <!-- author -->
      <text class="author" x="130" y="1049" textLength="498" lengthAdjust="spacing">BY DR. LENA MARSH</text>
    </svg>
  </div>
</body>
</html>
```